Copper Lantern Consulting Wordpress Website Design

I am looking for a wordpress website design for a consulting company called Copper Lantern Consulting. Services include SEO, social media campaign, PPC, and other online services. I want a media savvy looking website that is very easy to navigate but still looks professional. I'm essentially looking to have the clients say "wow" when they see the website but still can get an idea of the services they offer as a company. colour scheme should be blue and white primarily as the logo will be blue and white (in the midst of getting it finalized).

Target Market(s)

B2B, business owners and decision makers for SEO, PPC, Social Media, Etc.

Industry/Entity Type

Business Consultant

Colors
0293ce
33a6d7
0255a3
3276b5
85acd3
ffffff

Requirements
Must have
• Must look sleek and "techy" but at the same time look stylish and media savvy.
Nice to have
• blue and white as the colour scheme to a degree. Just an idea considering the logo will be blue and white. Perhaps some nice high resolution photos, some sliders
• also looking for potentially having large icons that represent some of the services we provide so its easy for clients to know what we offer.
Should not have
• bubbly and fun. This is more of a professional website.

```html
<!DOCTYPE html>
<html lang="en">
<head>
<meta charset="utf-8">
<title>Copper Lantern Consulting</title>
<link href="https://fonts.googleapis.com/css2?family=Open+Sans:wght@300;400;600;700&display=swap" rel="stylesheet">
<style>
:root{
  --blue:#0255a3;
  --blue-mid:#3276b5;
  --sky:#0293ce;
  --sky-soft:#33a6d7;
  --pale:#85acd3;
  --white:#ffffff;
  --ink:#333;
  --muted:#888;
  --line:#e3e3e3;
  --footer:#2b2b2b;
}
*{box-sizing:border-box;margin:0;padding:0}
html,body{width:759px;height:1200px;overflow:hidden}
body{font-family:'Open Sans',Arial,sans-serif;color:var(--ink);background:var(--white);position:relative}

/* header */
.site-header{height:48px;display:flex;align-items:center;justify-content:space-between;padding:0 24px 0 30px;position:relative;background:var(--white)}
.brand{display:flex;align-items:center;gap:7px}
.brand-dot{width:22px;height:22px;border-radius:50%;background:var(--blue)}
.brand-name{font-size:10px;font-weight:700;color:var(--blue);line-height:1.05;text-transform:uppercase;letter-spacing:.3px}
.header-right{display:flex;flex-direction:column;align-items:flex-end}
.header-top{position:absolute;top:6px;right:24px;display:flex;align-items:center;gap:8px;font-size:7px;color:var(--muted)}
.btn-login{background:var(--blue);color:var(--white);font-size:7px;font-weight:600;padding:4px 14px}
.main-nav{display:flex;gap:24px;margin-top:26px}
.main-nav a{font-size:7px;font-weight:600;color:var(--ink);text-decoration:none;text-transform:uppercase;padding-bottom:4px}
.main-nav a.active{color:var(--blue);border-bottom:2px solid var(--blue)}

/* hero */
.hero{position:relative;height:355px;background:linear-gradient(120deg,#c9d3dc 0%,#9aa8b6 40%,#d9dfe4 70%,#8d9aa6 100%)}
.hero::after{content:"";position:absolute;inset:0;background:rgba(30,45,65,.35)}
.hero-content{position:absolute;left:0;right:0;top:105px;text-align:center;color:var(--white);z-index:1}
.hero-mark{width:58px;height:58px;border-radius:50%;border:3px solid var(--white);margin:0 auto 12px}
.hero-title{font-size:26px;font-weight:300;letter-spacing:1px;text-transform:uppercase}
.hero-text{font-size:8px;width:270px;margin:8px auto 0;line-height:1.5}

/* section titles */
.section-title{text-align:center;font-size:20px;font-weight:700;color:var(--ink);text-transform:uppercase}
.section-title span{color:var(--blue)}
.title-rule{width:50px;height:2px;background:var(--blue);margin:6px auto 0}

/* services */
.services{padding:24px 60px 0;height:240px}
.services-intro{text-align:center;font-size:7.5px;font-style:italic;color:var(--muted);margin-top:10px}
.service-list{display:flex;justify-content:space-between;margin-top:24px;padding:0 10px}
.service{width:130px;text-align:center}
.service-icon{width:46px;height:46px;border-radius:50%;background:var(--blue);margin:0 auto 10px;display:flex;align-items:center;justify-content:center}
.service h3{font-size:8px;font-weight:700;text-transform:uppercase}
.service p{font-size:7px;color:var(--muted);margin-top:5px;line-height:1.5}

/* what we do */
.work{padding:38px 60px 0;height:342px;border-top:1px solid var(--line)}
.work-grid{display:flex;justify-content:space-between;margin-top:22px}
.work-card{width:192px}
.work-photo{height:112px;border:4px solid #f0f0f0}
.work-photo.one{background:linear-gradient(135deg,#cfd8e2,#8fa3b8)}
.work-photo.two{background:linear-gradient(135deg,#d8cfc6,#a58f7c)}
.work-photo.three{background:linear-gradient(135deg,#dfe5ea,#9db0c0)}
.work-card h3{font-size:8px;font-weight:700;text-transform:uppercase;margin-top:10px}
.work-card p{font-size:7px;color:var(--muted);line-height:1.55;margin-top:5px}
.btn-more{display:inline-block;background:var(--blue);color:var(--white);font-size:6.5px;font-weight:600;padding:5px 12px;margin-top:10px;text-transform:uppercase}

/* partners */
.partners{height:190px;background:#f6f6f6;padding:28px 40px 0;position:relative}
.partner-row{display:flex;align-items:center;justify-content:space-between;margin-top:24px}
.arrow{width:14px;color:#aaa;font-size:18px;text-align:center}
.partner{width:110px;height:54px;background:var(--white);border:1px solid var(--line);display:flex;align-items:center;justify-content:center;font-size:13px;font-weight:600;color:#777}

/* footer */
.site-footer{position:absolute;left:0;right:0;bottom:0;height:75px;background:var(--footer);color:#bbb;display:flex;align-items:center;justify-content:space-between;padding:0 40px}
.footer-call small,.footer-mail small{display:block;font-size:7px;color:#999}
.footer-call strong{font-size:14px;color:var(--sky-soft);font-weight:700}
.footer-mail span{font-size:7px}
.social{display:flex;gap:5px}
.social i{width:16px;height:16px;border-radius:50%;background:#ddd;display:block}
.copyright{font-size:7px;color:#999;text-align:right;line-height:1.5}
</style>
</head>
<body>

<header class="site-header">
  <div class="brand">
    <div class="brand-dot"></div>
    <div class="brand-name">Copper Lantern<br>Consulting</div>
  </div>
  <div class="header-top">
    <span>+1 402 555 0186</span>
    <span class="btn-login">LOGIN</span>
  </div>
  <nav class="main-nav">
    <a class="active" href="#">Home</a>
    <a href="#">Who we are</a>
    <a href="#">Services</a>
    <a href="#">Clients and partners</a>
    <a href="#">Contact us</a>
  </nav>
</header>

<section class="hero" role="img" aria-label="Photo of a team of consultants working together around a laptop in a bright office">
  <div class="hero-content">
    <div class="hero-mark"></div>
    <h1 class="hero-title">Copper Lantern Consulting</h1>
    <p class="hero-text">Lorem Ipsum is simply dummy text of the printing and typesetting industry. Lorem Ipsum has been the industry's standard dummy text.</p>
  </div>
</section>

<section class="services">
  <h2 class="section-title">Our <span>Services</span></h2>
  <div class="title-rule"></div>
  <p class="services-intro">Lorem ipsum is simply dummy text of the printing and typesetting standard dummy text ever since the 1500s.</p>
  <div class="service-list">
    <div class="service">
      <div class="service-icon"><svg width="20" height="20" viewBox="0 0 20 20" fill="none" stroke="#fff" stroke-width="2"><circle cx="8" cy="8" r="5"/><path d="M12 12l5 5"/></svg></div>
      <h3>SEO</h3>
      <p>We take the time to understand your business culture.</p>
    </div>
    <div class="service">
      <div class="service-icon"><svg width="20" height="20" viewBox="0 0 20 20" fill="#fff"><circle cx="5" cy="10" r="2.5"/><circle cx="15" cy="5" r="2.5"/><circle cx="15" cy="15" r="2.5"/><path d="M5 10L15 5M5 10l10 5" stroke="#fff" stroke-width="1.5"/></svg></div>
      <h3>Social Media Campaign</h3>
      <p>We take the time to understand your business culture.</p>
    </div>
    <div class="service">
      <div class="service-icon"><svg width="20" height="20" viewBox="0 0 20 20" fill="none" stroke="#fff" stroke-width="2"><path d="M15 7a6 6 0 0 0-10 0M5 13a6 6 0 0 0 10 0"/><path d="M15 3v4h-4M5 17v-4h4"/></svg></div>
      <h3>PPC</h3>
      <p>We take the time to understand your business culture.</p>
    </div>
    <div class="service">
      <div class="service-icon"><svg width="20" height="20" viewBox="0 0 20 20" fill="none" stroke="#fff" stroke-width="1.6"><circle cx="10" cy="10" r="7"/><ellipse cx="10" cy="10" rx="3" ry="7"/><path d="M3 10h14"/></svg></div>
      <h3>Online Services</h3>
      <p>We take the time to understand your business culture.</p>
    </div>
  </div>
</section>

<section class="work">
  <h2 class="section-title">What <span>We Do</span></h2>
  <div class="title-rule"></div>
  <div class="work-grid">
    <article class="work-card">
      <div class="work-photo one" role="img" aria-label="Photo of people working at computers in an office"></div>
      <h3>Pharus bougreum et malorem</h3>
      <p>Lorem Ipsum is simply dummy text of the printing and typesetting industry. Lorem Ipsum has been the industry's standard dummy text.</p>
      <span class="btn-more">Read more</span>
    </article>
    <article class="work-card">
      <div class="work-photo two" role="img" aria-label="Photo of hands with a notebook and coffee on a desk"></div>
      <h3>Accusamus et justo odio</h3>
      <p>Lorem Ipsum is simply dummy text of the printing and typesetting industry. Lorem Ipsum has been the industry's standard dummy text.</p>
      <span class="btn-more">Read more</span>
    </article>
    <article class="work-card">
      <div class="work-photo three" role="img" aria-label="Photo of a business meeting around a table"></div>
      <h3>Blanditiis praesentium volupt</h3>
      <p>Lorem Ipsum is simply dummy text of the printing and typesetting industry. Lorem Ipsum has been the industry's standard dummy text.</p>
      <span class="btn-more">Read more</span>
    </article>
  </div>
</section>

<section class="partners">
  <h2 class="section-title">Our <span>Partners</span></h2>
  <div class="title-rule"></div>
  <div class="partner-row">
    <span class="arrow">&#8249;</span>
    <div class="partner">Norvane</div>
    <div class="partner">Brightfold</div>
    <div class="partner">Tallowmark</div>
    <div class="partner">Quillstone</div>
    <div class="partner">Harbrook</div>
    <span class="arrow">&#8250;</span>
  </div>
</section>

<footer class="site-footer">
  <div class="footer-call"><small>Call us at</small><strong>1-800-555-0142</strong></div>
  <div class="footer-mail"><small>Email</small><span>hello@copperlantern.example</span></div>
  <div class="social"><i></i><i></i><i></i><i></i><i></i></div>
  <div class="copyright">Copyright © 2015 copperlantern.example<br>All rights reserved. privacy policy</div>
</footer>

</body>
</html>
```